PPT Design Project for an educational startup

We seek a PPT design for a new company based in Japan called "Brivorent".
We provide PPT slide-based educational videos for free.
Please see the link below. You will see some videos.
http://velmora-example.jp/
The current template is also attached.
As we are changing our service name from Velmora to Brivorent, we are considering to change the PPT template as well.
Here are some notes regarding this project.
1. We need three pages;
- Title page: Letters for the tile and the logo are necessary. Some pictorial marks or other design would be appreciated.
- Contents page: Just one line to divide the message part and contents part should be sufficient. Please do not spend your time here.
- Final page: The word "Thank you for watching!" in the center. Some pictorial marks or other design would be appreciated.
2. Please use light green, orange, and purple as main colors. (Same as the current template)
3. You don't have to think about the font-style. This is going to be Japanese font, so we will take care of this.
4. Background color needs to be white, as the slides could be printed out.
5. We use Powerpoint for Mac.
6. No copyright section required, as these slides will be creative commons. Instead of the copyright section, please put the creative commons mark in all slides. (which is in the original template attached)
Updates
Please forget about the creative commons mark.
Hi all,
Target Market(s)
16-25 years old people, who are highly educated or highly motivated for education
Industry/Entity Type
It Company
Requirements
Must have
- 1. Creative commons mark (which is in the original template)
Should not have
- 1. Copyright mark

```html
<!DOCTYPE html>
<html lang="en">
<head>
<meta charset="utf-8">
<title>Brivorent – Final Slide</title>
<link rel="stylesheet" href="https://fonts.googleapis.com/css2?family=Alegreya:wght@500&family=Open+Sans:wght@700&display=swap">
<style>
  :root {
    --slide-bg: #ffffff;
    --rail-grey: #7f7f7f;
    --accent-orange: #f39a4c;
    --accent-green: #8cbf4f;
    --title-purple: #7d5fa6;
    --brand-grey: #7a7a7a;
  }
  * { margin: 0; padding: 0; box-sizing: border-box; }
  html, body { width: 1200px; height: 900px; overflow: hidden; background: var(--slide-bg); }
  .slide { position: relative; width: 1200px; height: 900px; background: var(--slide-bg); }
  .side-rail { position: absolute; left: 0; top: 0; width: 25px; height: 885px; background: var(--rail-grey); }
  .header-rule { position: absolute; left: 0; top: 86px; width: 1200px; height: 3px; background: var(--accent-orange); }
  .footer-band { position: absolute; left: 0; top: 885px; width: 1200px; height: 15px; background: var(--accent-orange); }
  .footer-band-accent { position: absolute; left: 1052px; top: 882px; width: 148px; height: 18px; background: var(--accent-green); }
  .closing-message {
    position: absolute; left: 0; top: 412px; width: 1200px;
    text-align: center;
    font-family: "Alegreya", Georgia, serif;
    font-weight: 500; font-size: 56px; line-height: 70px;
    color: var(--title-purple);
  }
  .brand-name {
    position: absolute; right: 14px; top: 846px;
    font-family: "Open Sans", Arial, sans-serif;
    font-weight: 700; font-size: 26px; line-height: 32px;
    color: var(--brand-grey);
  }
</style>
</head>
<body>
  <main class="slide">
    <div class="side-rail"></div>
    <div class="header-rule"></div>
    <p class="closing-message">Thank you for watching!</p>
    <div class="brand-name">Brivorent</div>
    <div class="footer-band"></div>
    <div class="footer-band-accent"></div>
  </main>
</body>
</html>
```